WE are a specialised tutoring business looking to a have a landing page design

we need a landing page designed for our business. We provide specialised tutoring for children with learning difficulties. I have attached a brief which includes our logo and also the content for the page.

Target Market(s)

parents

Number of Pages Required

1 page

Requirements
Must have
• our existing logo and the content provided

```html
<!DOCTYPE html>
<html lang="en">
<head>
<meta charset="utf-8">
<title>brightnest – specialised learning for children</title>
<link href="https://fonts.googleapis.com/css2?family=Lato:wght@400;700&display=swap" rel="stylesheet">
<style>
  :root {
    --green: #7bbf3a;
    --green-title: #6cb83a;
    --text-dark: #2b2b2b;
    --text-muted: #444444;
    --white: #ffffff;
    --hero-deep: #3b2f28;
    --hero-warm: #6a3b30;
    --hero-red: #8e2a33;
    --band-teal: #1d6a78;
    --band-green: #158a3a;
    --icon-grey: #555555;
    --icon-tone: #d9d9d9;
  }
  * { box-sizing: border-box; margin: 0; padding: 0; }
  html, body { width: 931px; height: 1200px; overflow: hidden; background: var(--white); }
  body { font-family: "Lato", sans-serif; color: var(--text-dark); }
  .page { position: relative; width: 931px; height: 1200px; }

  .hero { position: absolute; left: 0; top: 0; width: 931px; height: 574px; }
  .hero-photo {
    position: absolute; inset: 0;
    background:
      linear-gradient(rgba(0,0,0,0.28), rgba(0,0,0,0.28)),
      linear-gradient(100deg, var(--hero-deep) 0%, var(--hero-warm) 45%, var(--hero-red) 75%, var(--hero-warm) 100%);
  }
  .brand { position: absolute; top: 24px; left: 0; width: 100%; text-align: center; color: var(--white); }
  .brand-dot { display: block; width: 44px; height: 44px; margin: 0 auto 14px; border-radius: 50%; background: var(--green); }
  .brand-name { font-size: 40px; font-weight: 400; line-height: 1; letter-spacing: -0.5px; }
  .brand-tagline { margin-top: 10px; font-size: 11px; letter-spacing: 2.4px; }

  .hero-headline {
    position: absolute; top: 260px; left: 130px; width: 671px;
    text-align: center; color: var(--white);
    font-size: 24px; font-weight: 700; line-height: 32px;
  }
  .signup { position: absolute; top: 417px; left: 175px; display: flex; gap: 12px; }
  .signup-field {
    width: 210px; height: 37px; background: var(--white); border: none;
    padding: 0 12px; font-family: "Lato", sans-serif; font-size: 12px; color: #555;
    display: flex; align-items: center;
  }
  .signup-submit {
    width: 140px; height: 37px; background: var(--green); color: var(--white);
    font-size: 16px; font-weight: 700; display: flex; align-items: center; justify-content: center;
  }

  .features { position: absolute; top: 620px; left: 0; width: 931px; }
  .feature { position: absolute; top: 0; width: 260px; text-align: center; }
  .feature:nth-child(1) { left: 56px; }
  .feature:nth-child(2) { left: 335px; }
  .feature:nth-child(3) { left: 615px; }
  .feature-icon { width: 64px; height: 64px; margin: 0 auto; border-radius: 6px; background: var(--icon-tone); }
  .feature-title { margin-top: 17px; font-size: 18px; font-weight: 700; color: var(--green-title); }
  .feature-text { margin-top: 6px; font-size: 12px; line-height: 20px; color: var(--text-dark); }

  .contact {
    position: absolute; top: 955px; left: 0; width: 931px; height: 160px;
    background: linear-gradient(90deg, var(--band-teal) 0%, #1a7a5a 50%, var(--band-green) 100%);
    color: var(--white); text-align: center;
  }
  .contact-title { position: absolute; top: 32px; width: 100%; font-size: 21px; font-weight: 700; }
  .contact-line { position: absolute; width: 100%; font-size: 13px; display: flex; justify-content: center; align-items: center; gap: 10px; }
  .contact-line.address { top: 72px; }
  .contact-line.email { top: 98px; }
  .contact-line svg { fill: var(--white); }

  .footer { position: absolute; top: 1136px; left: 0; width: 931px; text-align: center; }
  .copyright { font-size: 10px; color: var(--text-muted); }
  .social { margin-top: 12px; display: flex; justify-content: center; align-items: center; gap: 16px; }
  .social-dot { width: 15px; height: 15px; border-radius: 50%; background: var(--icon-grey); }
  .social svg { fill: var(--icon-grey); }
</style>
</head>
<body>
<div class="page">
  <section class="hero">
    <div class="hero-photo" role="img" aria-label="Photo of a tutor helping a boy read a book in a library"></div>
    <div class="brand">
      <span class="brand-dot"></span>
      <div class="brand-name">brightnest</div>
      <div class="brand-tagline">specialised learning for children</div>
    </div>
    <h1 class="hero-headline">brightnest is a team of psychologists and teachers focused on supporting children with social, emotional, and learning difficulties. We provide specialised tutoring and support for children and their families.</h1>
    <form class="signup">
      <div class="signup-field">Enter Email Address</div>
      <div class="signup-field">Enter Phone No</div>
      <div class="signup-submit">Submit</div>
    </form>
  </section>

  <section class="features">
    <article class="feature">
      <div class="feature-icon" role="img" aria-label="Line icon of two children"></div>
      <h2 class="feature-title">Know the Child</h2>
      <p class="feature-text">We are dedicated to evidence-based assessment and diagnosis. We believe that early intervention requires a clear understanding of the unique challenges faced by the child. This involves assessment and also a dedication to working with children, their parents, and also their preschool and school contexts. This allows us to ensure that any intervention is tailored to the child.</p>
    </article>
    <article class="feature">
      <div class="feature-icon" role="img" aria-label="Line icon of a child reading a book"></div>
      <h2 class="feature-title">Meet the Need</h2>
      <p class="feature-text">We provide individualised tutoring for children that focuses on their specific areas of learning need. Our team are dedicated to providing best-practice learning support within an environment of encouragement and care, understanding the impact that learning difficulties can have on broader areas of confidence and self-concept.</p>
    </article>
    <article class="feature">
      <div class="feature-icon" role="img" aria-label="Line icon of a child in front of a castle"></div>
      <h2 class="feature-title">Watch them Grow</h2>
      <p class="feature-text">We are committed to seeing growth, this requiring strategic intervention and the ability to assess and provide evidence of achievement. Our passion is not only to provide effective support, but also to help children and their families to see this growth, fostering a culture of positivity and engagement in learning.</p>
    </article>
  </section>

  <section class="contact">
    <h2 class="contact-title">Contact Details:</h2>
    <div class="contact-line address">
      <svg width="9" height="12" viewBox="0 0 9 12" aria-hidden="true"><path d="M4.5 0A4.5 4.5 0 0 0 0 4.5C0 8 4.5 12 4.5 12S9 8 9 4.5A4.5 4.5 0 0 0 4.5 0Zm0 6.3a1.8 1.8 0 1 1 0-3.6 1.8 1.8 0 0 1 0 3.6Z"/></svg>
      <span>12/48 Harbour View Road, Lakeside, 2150</span>
    </div>
    <div class="contact-line email">
      <svg width="13" height="10" viewBox="0 0 13 10" aria-hidden="true"><path d="M0 0h13v1.5L6.5 5.5 0 1.5Z"/><path d="M0 3l6.5 4L13 3v7H0Z"/></svg>
      <span>info@brightnestlearning.com.au</span>
    </div>
  </section>

  <footer class="footer">
    <p class="copyright">Copyright © 2019, Company Name. All Right reserved</p>
    <div class="social">
      <span class="social-dot" aria-label="Social profile"></span>
      <svg width="18" height="13" viewBox="0 0 18 13" aria-label="Email"><path d="M0 0h18v2L9 7.5 0 2Z"/><path d="M0 4l9 5.5L18 4v9H0Z"/></svg>
      <span class="social-dot" aria-label="Social profile"></span>
      <span class="social-dot" aria-label="Social profile"></span>
      <span class="social-dot" aria-label="Social profile"></span>
    </div>
  </footer>
</div>
</body>
</html>
```